LeaseWiser - Apartment Reviews Website Concept Sketch

IMPORTANT UPDATES BELOW -

Current Contest:
Deliverable: 1 or more original design concepts for website home-page. A guaranteed payment will be made to the lead design.

Context:
This guaranteed-payment contest is for submission of 1 or more concept sketches for the home page of the website described below.

Based on finalist submissions, a freelance contract may be let for design-only development (PSDs only) of the full site, approximately 20 pages. Budget for the full site design is $3000 - $5000 and will include multiple rounds to refine the home-page concept and then to extend the design to the full site.

All mySql and PHP logic is already coded and working. No coding is required for the contest or the follow-on project.

IMPORTANT UPDATES ABOVE -

The Website:

LeaseWiser is developing an on-line, searchable, pay-for-access database of user-contributed reviews of apartment complexes. Consumers will use these reviews to make better informed decisions before committing to an apartment lease.

We currently have a functional, wireframe-only website accessible at leasewiser.example. The wireframes are under development, and site pages may display debugging information or may be inaccessible on occasion.

Additional information as well as a site map is available at: leasewiser.example/qqstudio.

We require complete graphic design for a multi-page, interactive, database-driven website. Cutting and coding the design into the existing php code base is a separate project, but feel free to quote on this separately if you have capabilities. We do not require any software or database development. All software is proprietary, we are not using any third-party platform for CMS, survey management, etc.

Attributes we wish to convey with our logo, website, and other presentation:
• Trustworthiness – users should expect the information we present to be accurate and complete
• Impartiality - users can rely on the survey results we present not to be influenced or “bought” by apartment managers
• Professionalism – LeaseWiser is a team of professionals dedicated to building and delivering a high-value, high-relevance database of fresh information that will help apartment renters make better decisions about where to live. We are not an informal community, not a group of volunteers, and not a free-access, open source product.
• Simplicity – our site is easy to use, easy to search, and our survey results are easy to understand
• Accessibility – anyone can use our service, it is not just for experts or people with technical skills
• Affordability – our service is priced at a point (about $50 for 90-days use) that it is affordable for everyone who plans to rent an apartment and makes economic sense as insurance against making an uninformed decision (much less than the cost of a month’s rent)
• Interest to Apartment Dwellers – our name, and preferably our logo, identifies us immediately as being of interest to apartment renters and seekers
• Positive Outlook – although the greatest value of LeaseWiser will be in helping apartment hunters avoid buildings with construction, management, and neighborhood problems, our website imagery should not focus on the negative aspects, but rather on the happiness, security, and satisfaction that comes with a good selection of an apartment

Website Purpose
During Phase 1 (current) of LeaseWiser’s development, the purpose of the website is to collect apartment reviews. Traffic will be driven by a display/performance ad campaign. We are assembling a business asset (the database) and this is really a direct response marketing campaign. We will offer a variety of incentives (sweepstakes entries, gift card redemption) to induce people to complete a survey and view a series of advertising offers. During Phase 1, there will be no database of apartment reviews for users to preview, and nothing for us to sell.

During Phase 2 (future) of LeaseWiser’s development, the purpose of the website will be to induce members to pay to access the database, and to provide a means for paying customers to access the database of reviews. Phase 2 is NOT in scope at this time, but will represent a substantial future upgrade - naturally the original design team will be in a strong competitive position for this future work.

The LeaseWiser website has a small area that will serve our advertising partners so they can access campaign and reporting information. This part of the site will need a simple but professional design treatment and is within the scope of Phase 1 development.

Our primary creative goal at this time is to present a website that supports Phase 1 goals. Many of the pages necessary for Phase 2 operation are outside the scope of the Phase 1 creative effort, in particular previewing reviews, searching the database, viewing search results, and transaction-oriented pages.
Updates

Project Deadline Extended
Reason: We didn't communicate the nature of the Design Contest well. We are extending the deadline to permit designers to re-evaluate the scope of the current work in the context of the award amount.

Target Market(s)

Our market audience is internet-savvy Americans who live in or are moving into an apartment.

Industry/Entity Type

Graphic Design

Requirements
Must have
• We are finalizing logo design and have posted a draft copy on the site. Logo design is still subject to refinement, but the basic concept is frozen. Colors / combinations may change, but will be arena of blue or blue+green.

Key elements of the home page are:
- a call to action to review an apartment
- room for 1-2 rotating articles about selecting an apartment, planning a move, shopping for insurance in your new location, etc. to act as light-weight, added value elements for site visitors.

Important to know:
- The survey itself (reviewapartment.php - only accessible by following all the steps starting with the "review an apartment" link) is database-driven, so the design must be able to accommodate assembly of questions in different formats using a building-block approach. The current wire-frame illustrates the major question/answer formats: radio; checkbox; matrix-radio; free-text.

Over the life of the project, we will undoubtedly build dozens of landing pages that center around the call to action of "review the apartment where you live" with various inducements (sweepstakes entry, redeemable incentives, social appeals, etc.) Development of these landing pages is a separate project, but the initial design should include one or two. If direct-marketing design / landing page design is not your forte, these pages can be removed from the scope of the web design project.

Should not have
• We would prefer to stay away from flash-heavy pages for the website.

```html
<!DOCTYPE html>
<html lang="en">
<head>
<meta charset="utf-8">
<title>LeaseWiser – Apartment Reviews</title>
<link href="https://fonts.googleapis.com/css2?family=Open+Sans:ital,wght@0,300;0,400;0,600;0,700;0,800;1,400&display=swap" rel="stylesheet">
<style>
:root{
  --page-green:#62c94a;
  --brand-green:#6fb51f;
  --brand-blue:#1b5eb0;
  --nav-blue:#1e4f8f;
  --nav-blue-light:#3c78b5;
  --panel-dark:#555555;
  --label-yellow:#e6ef8f;
  --button-green:#3fbd1f;
  --link-blue:#1f6fc1;
  --sky-blue:#1c99ef;
  --text-dark:#333333;
  --text-grey:#7d7d7d;
  --row-light:#eeeeee;
  --row-mid:#e2e2e2;
}
*{box-sizing:border-box;margin:0;padding:0}
html,body{width:1200px;height:856px;overflow:hidden}
body{background:var(--page-green);font-family:"Open Sans",Arial,sans-serif;position:relative}
.site{position:absolute;left:53px;top:26px;width:1085px;height:850px;background:#fff;border-radius:10px 10px 0 0;overflow:hidden;box-shadow:0 0 4px rgba(0,0,0,.25)}
.abs{position:absolute;white-space:nowrap}

/* header */
.brand{left:30px;top:40px;display:flex;align-items:center;gap:10px}
.brand-mark{width:22px;height:22px;background:var(--brand-green)}
.brand-name{font-size:34px;font-weight:800;color:var(--brand-blue);letter-spacing:-1px}
.tagline{left:273px;top:66px;font-size:19px;font-style:italic;color:var(--text-grey)}
.util-links{left:596px;top:22px;font-size:12px;color:var(--sky-blue)}
.util-links span{margin:0 7px;color:#9bc9ec}
.survey-btn{left:888px;top:17px;width:182px;height:32px;border-radius:4px;background:linear-gradient(#3fb6ff,#1588e0);color:#fff;font-weight:700;font-size:16px;text-align:center;line-height:32px}
.account{left:881px;top:81px;font-size:12px;font-weight:700;color:#333;display:flex;align-items:center;gap:8px}
.login-btn{background:linear-gradient(#ff9d3a,#f3760d);color:#fff;padding:0 10px;height:26px;line-height:26px;border-radius:2px}

/* nav */
.main-nav{left:0;top:123px;width:1085px;height:40px;background:linear-gradient(var(--nav-blue-light),var(--nav-blue));display:flex;color:#fff;font-weight:700;font-size:16px}
.main-nav a{padding:0 18px;line-height:40px;color:#fff;text-decoration:none}
.main-nav .active{background:linear-gradient(#4daa24,#2e8410);width:89px;text-align:center;padding:0}
.main-nav .my-account{margin-left:auto;width:136px;text-align:center;padding:0;background:linear-gradient(#5d8fc2,#3f70a5)}

/* hero */
.hero{left:0;top:163px;width:673px;height:321px;background:linear-gradient(180deg,#4f8fd6 0%,#8ab8e4 40%,#6c7a5e 75%,#3a3a35 100%)}
.hero-caption{left:0;top:418px;width:673px;height:66px;background:rgba(0,0,0,.7)}
.hero-title{left:12px;top:424px;color:#fff;font-size:17px}
.hero-reviews{left:16px;top:454px;color:#5ab6ff;font-size:11px;font-weight:700}
.read-more{left:93px;top:451px;background:#6fbcf5;color:#0a2d55;font-size:11px;font-weight:700;padding:2px 9px}
.thumb{top:432px;width:47px;height:47px;background:linear-gradient(#6aa0d8,#c8cfd3);border:2px solid #fff}

/* search */
.search-title{left:685px;top:165px;font-size:27px;font-weight:400;color:var(--brand-green)}
.search-title b{font-weight:400;color:var(--brand-blue)}
.search-panel{left:681px;top:215px;width:396px;height:240px;background:var(--panel-dark);border-radius:4px}
.field-label{left:685px;width:133px;color:var(--label-yellow);font-weight:700;font-size:14.5px;letter-spacing:-.3px;text-align:right;line-height:36px;height:36px}
.input{background:#fff;border-radius:3px;height:36px;font-size:13px;display:flex;align-items:center;padding:0 8px;justify-content:space-between}
.caret{width:0;height:0;border-left:6px solid transparent;border-right:6px solid transparent;border-top:7px solid #555}
.search-btn{left:935px;top:406px;width:132px;height:42px;border-radius:3px;background:linear-gradient(#5ad63a,var(--button-green));color:#fff;font-weight:700;font-size:15px;text-align:center;line-height:42px}

/* featured */
.featured-bar{left:0;top:484px;width:673px;height:51px;background:linear-gradient(#a9dd6c,#70bd2e)}
.featured-title{left:14px;top:489px;font-size:30px;font-weight:300;color:#1c2a10}
.bar-btn{left:573px;top:491px;width:95px;height:38px;border-radius:3px;background:#2f8c13;color:#d8f5b6;font-size:16px;line-height:38px;text-align:center}
.card{top:552px;width:145px}
.card-photo{height:145px}
.card-title{margin-top:12px;font-size:12.5px;font-weight:700;color:var(--brand-green);line-height:17px;height:34px;white-space:nowrap;letter-spacing:-.2px}
.card-reviews{margin-top:10px;font-size:12px;font-weight:700;color:var(--link-blue);text-decoration:underline}
.card-btn{margin-top:16px;height:30px;border-radius:3px;background:linear-gradient(#4cc52a,#2e9a12);color:#fff;font-weight:700;font-size:13px;text-align:center;line-height:30px}

/* ad */
.ad-box{left:681px;top:491px;width:397px;height:160px;border:1px solid #8a8a8a;padding:7px}
.ad-art{width:100%;height:100%;background:linear-gradient(90deg,#f39a00,#ffc21a)}
.ad-text{left:833px;top:510px;width:236px;height:98px;background:rgba(70,40,0,.9);border-radius:10px 0 0 10px;padding:4px 18px;color:#fff}
.ad-text h3{font-size:48px;font-weight:700;line-height:56px}
.ad-text p{font-size:11px;font-weight:700}
.ad-sponsor{left:981px;top:613px;width:82px;height:28px;background:#fff;color:var(--brand-blue);font-size:15px;font-weight:600;text-align:center;line-height:28px}

/* top rated */
.top-rated{left:681px;top:662px;width:396px}
.top-rated h2{height:55px;background:linear-gradient(#3c78c3,#15427f);color:#fff;font-weight:300;font-size:28px;line-height:55px;padding-left:8px}
.rank-row{height:39px;display:flex;justify-content:space-between;align-items:center;padding:0 12px;font-size:13px;color:var(--text-dark);border-bottom:1px solid #fff}
.rank-row:nth-child(odd){background:var(--row-mid)}
.rank-row:nth-child(even){background:var(--row-light)}
.rank-row a{font-size:11px;color:var(--link-blue);text-decoration:underline}
</style>
</head>
<body>
<div class="site">
  <header>
    <div class="abs brand"><span class="brand-mark"></span><span class="brand-name">LeaseWiser</span></div>
    <div class="abs tagline">“Before you rent, hear what the neighbors say”</div>
    <div class="abs util-links">Privacy policy<span>|</span>Terms &amp; Conditions<span>|</span>FAQ</div>
    <div class="abs survey-btn">Take Your Survey</div>
    <div class="abs account">CREATE AN ACCOUNT <span class="login-btn">LOGIN</span></div>
  </header>

  <nav class="abs main-nav">
    <a class="active">Home</a><a>About Us</a><a>Look Up Apartments</a><a>Enter Sweeps</a><a>Contest Rurle</a><a class="my-account">My Account</a>
  </nav>

  <section>
    <div class="abs hero" role="img" aria-label="Photo of a white two-storey suburban house under a blue sky"></div>
    <div class="abs hero-caption"></div>
    <div class="abs hero-title">RIO GRANDE VALLEY HOUSING ESTATE</div>
    <div class="abs hero-reviews">21 Reviews</div>
    <div class="abs read-more">READ MORE</div>
    <div class="abs thumb" style="left:442px" role="img" aria-label="House thumbnail"></div>
    <div class="abs thumb" style="left:495px;opacity:.8" role="img" aria-label="House thumbnail"></div>
    <div class="abs thumb" style="left:548px;opacity:.8" role="img" aria-label="House thumbnail"></div>
    <div class="abs thumb" style="left:601px;opacity:.8" role="img" aria-label="House thumbnail"></div>
  </section>

  <section>
    <h1 class="abs search-title">Find Perfect Home for <b>RENT</b></h1>
    <div class="abs search-panel"></div>
    <div class="abs field-label" style="top:223px">FAND A HOME IN</div>
    <div class="abs input" style="left:822px;top:223px;width:247px;color:#888">Place or Postcode</div>
    <div class="abs field-label" style="top:265px">BEDROOM</div>
    <div class="abs input" style="left:822px;top:265px;width:109px">3<span class="caret"></span></div>
    <div class="abs field-label" style="top:307px">BATHROOM</div>
    <div class="abs input" style="left:822px;top:307px;width:109px">2<span class="caret"></span></div>
    <div class="abs field-label" style="top:349px">BUDGET</div>
    <div class="abs input" style="left:822px;top:349px;width:109px">$400<span class="caret"></span></div>
    <div class="abs" style="left:937px;top:361px;font-size:10px;color:#ccc;font-weight:700">TO</div>
    <div class="abs input" style="left:959px;top:349px;width:110px">$600<span class="caret"></span></div>
    <div class="abs search-btn">SEARCH</div>
  </section>

  <section>
    <div class="abs featured-bar"></div>
    <h2 class="abs featured-title">Featured Homes</h2>
    <div class="abs bar-btn">View More</div>

    <div class="abs card" style="left:20px">
      <div class="card-photo" role="img" aria-label="Photo of a two-storey family house with lawn" style="background:linear-gradient(#5f9ad8,#7aa86a)"></div>
      <div class="card-title">3BHK Nort Facing<br>Appartment</div>
      <div class="card-reviews">8 Reviews</div>
      <div class="card-btn">View More</div>
    </div>
    <div class="abs card" style="left:184px">
      <div class="card-photo" role="img" aria-label="Photo of a villa with a swimming pool" style="background:linear-gradient(#b7d7ee,#e8dcc4 60%,#3fb0d8)"></div>
      <div class="card-title">4BHK apartment with<br>Swimming pool</div>
      <div class="card-reviews">6 Reviews</div>
      <div class="card-btn">View More</div>
    </div>
    <div class="abs card" style="left:349px">
      <div class="card-photo" role="img" aria-label="Photo of a house with a garage" style="background:linear-gradient(#7fb6e6,#cfa460 60%,#8a7a66)"></div>
      <div class="card-title">3BHK House in Ground<br>Floor with Garrage</div>
      <div class="card-reviews">6 Reviews</div>
      <div class="card-btn">View More</div>
    </div>
    <div class="abs card" style="left:514px">
      <div class="card-photo" role="img" aria-label="Photo of a large stone mansion" style="background:linear-gradient(#dbe8f2,#9b8063 60%,#c7c1b3)"></div>
      <div class="card-title">3BHK Nort Facing<br>Appartment</div>
      <div class="card-reviews">4 Reviews</div>
      <div class="card-btn">View More</div>
    </div>
  </section>

  <aside>
    <div class="abs ad-box"><div class="ad-art" role="img" aria-label="Illustration of hands holding a small house"></div></div>
    <div class="abs ad-text"><h3>Apply</h3><p>For your Home Loan in 5 min.</p></div>
    <div class="abs ad-sponsor">Northbank</div>

    <div class="abs top-rated">
      <h2>10 Top Rated Homes</h2>
      <div class="rank-row">3BHK North Facing Appartment<a>34 Reviews</a></div>
      <div class="rank-row">Long Living Room, 2 BHK Appartment<a>30 Reviews</a></div>
      <div class="rank-row">2 bedroom with Car Parking, Pool<a>30 Reviews</a></div>
    </div>
  </aside>
</div>
</body>
</html>
```